E-book named 'Lanterns Over Marrowby: Building Kinder Firms' needs cover

I need a cover for my ebook and also paper back book.
I need a very appealing cover for my ebook. Social enterprise is a company that gives something back to the society as opposed to only make profit.
The society and its people always benefit.
So far the above is the name chosen but I welcome small changes and ideas also a tag line would also be great something like “everything you need to know to sep up a social enterprise and succeed”
I want to write in the cover something to make people buy it. I want the name Social Enterprise in more evidence ...
Target Market(s)
Students, graduates and business minded people who are thinking of set up a social enterprise company and needs guidance
Industry/Entity Type
It Company
Colors
Designer to choose colors to be used in the design.
Look and feel
Each slider illustrates characteristics of the customer's brand and the style your logo design should communicate.

```html
<!DOCTYPE html>
<html lang="en">
<head>
<meta charset="utf-8">
<title>Lanterns Over Marrowby: Building Kinder Firms</title>
<link rel="stylesheet" href="https://fonts.googleapis.com/css2?family=Anton&family=Montserrat:wght@300;800&family=Oswald:wght@300&display=swap">
<style>
  :root {
    --cover-white: #ffffff;
    --brand-red: #c1272d;
    --brand-navy: #13305e;
    --globe-blue: #1c3f86;
    --globe-green: #3f7a3a;
    --hand-tone: #e0a97f;
  }
  html, body {
    margin: 0;
    padding: 0;
    overflow: hidden;
    background: var(--cover-white);
  }
  .cover {
    position: relative;
    width: 800px;
    height: 1200px;
    background: var(--cover-white);
    overflow: hidden;
  }
  .cover-type {
    position: absolute;
    left: 0;
    top: 0;
    width: 800px;
    height: 480px;
  }
  .author-band { fill: var(--brand-red); }
  .author-name {
    font-family: "Montserrat", sans-serif;
    font-weight: 300;
    fill: var(--cover-white);
  }
  .title-kicker {
    font-family: "Montserrat", sans-serif;
    font-weight: 800;
    fill: var(--brand-red);
  }
  .title-main {
    font-family: "Anton", sans-serif;
    fill: var(--brand-red);
  }
  .tagline-band { fill: var(--brand-navy); }
  .tagline {
    font-family: "Oswald", sans-serif;
    font-weight: 300;
    fill: var(--cover-white);
  }
  .hero-image {
    position: absolute;
    left: 16px;
    top: 608px;
    width: 768px;
    height: 592px;
    background:
      radial-gradient(circle at 52% 36%, var(--globe-blue) 0%, var(--globe-green) 28%, rgba(28,63,134,0.85) 40%, rgba(224,169,127,0.9) 56%, rgba(224,169,127,0.55) 78%, rgba(255,255,255,0) 100%);
  }
</style>
</head>
<body>
  <main class="cover">
    <svg class="cover-type" viewBox="0 0 800 480" xmlns="http://www.w3.org/2000/svg">
      <rect class="author-band" x="0" y="46" width="800" height="90"/>
      <text class="author-name" x="400" y="111" font-size="56" text-anchor="middle" textLength="584" lengthAdjust="spacingAndGlyphs">ODILE VARNHAGEN</text>

      <text class="title-kicker" x="32" y="226" font-size="46" textLength="736" lengthAdjust="spacingAndGlyphs">LANTERNS OVER MARROWBY:</text>
      <text class="title-main" x="32" y="372" font-size="152" textLength="736" lengthAdjust="spacingAndGlyphs">BUILDING KINDER FIRMS</text>

      <rect class="tagline-band" x="0" y="412" width="800" height="64"/>
      <text class="tagline" x="32" y="456" font-size="38" textLength="736" lengthAdjust="spacingAndGlyphs">Everything You Need To Know To Set Up a Social Enterprise and Succeed</text>
    </svg>

    <div class="hero-image" role="img" aria-label="Photograph of many children's hands reaching up together to hold a globe of the Earth showing the Americas"></div>
  </main>
</body>
</html>
```